Business card design needed

My business is in Matchmaking. My objective is to find the most compatible partner for my clients....basically I'm in the love and happiness industry bringing two people together for a lasting loving relationship.

I envision the design to be something with 2 people who are in love looking happy or even a silhouette.....I don't really know, I'm open to ideas.....maybe no picture at all, but I want it to be classy :-)

I do have a logo which I will upload. You can also go to my website to give you an idea on the colours and the design if that helps, however the website is not finished yet, it should be up by today or tomorrow. If the website has a heart with swirls on the upper left hand corner, that is the old website, please ignore that one. The one that will be up shortly has a picture frame on the home page with my logo that will be in the file I will upload on this page.

Target Market(s)

There are three categories: Over 45, Asian and Western and same sex, but would be able to afford to hire a matchmaker

Industry/Entity Type

Industry

Contact Information for Business Card

The Tidewell Bureau
Helping You Find The "One"
Maris Pelloway
Matchmaker
0491 572 064
info@tidewellbureau.com.au
www.tidewellbureau.com.au

```html
<!DOCTYPE html>
<html lang="en">
<head>
<meta charset="utf-8">
<title>The Tidewell Bureau – Business Card</title>
<link href="https://fonts.googleapis.com/css2?family=Open+Sans:wght@400;600;700&display=swap" rel="stylesheet">
<style>
  :root {
    --page-bg: #efefef;
    --card-white: #ffffff;
    --mauve: #7b5a78;
    --mauve-dark: #6a4a67;
    --teal: #6fae9f;
    --photo-light: #b9b9b9;
    --photo-mid: #6e6e6e;
    --photo-dark: #1c1c1c;
    --text-light: #ffffff;
  }
  * { box-sizing: border-box; margin: 0; padding: 0; }
  html, body {
    width: 1200px;
    height: 1000px;
    overflow: hidden;
    background: var(--page-bg);
    font-family: "Open Sans", Arial, sans-serif;
  }
  .card {
    position: absolute;
    left: 150px;
    top: 243px;
    width: 900px;
    height: 514px;
    background: var(--card-white);
    overflow: hidden;
    box-shadow: 0 6px 24px rgba(0,0,0,0.12);
  }
  .card-photo {
    position: absolute;
    inset: 0;
    background:
      radial-gradient(ellipse at 35% 55%, var(--photo-light) 0%, var(--photo-mid) 35%, transparent 70%),
      linear-gradient(135deg, var(--photo-dark) 0%, #3a3a3a 45%, var(--photo-dark) 100%);
  }
  .card-panel {
    position: absolute;
    inset: 0;
    clip-path: polygon(49% 0, 100% 0, 100% 100%, 43% 100%);
    background: var(--card-white);
  }
  .panel-edge {
    position: absolute;
    inset: 0;
    pointer-events: none;
  }
  .panel-band {
    position: absolute;
    left: 0;
    right: 0;
    top: 41%;
    bottom: 0;
    background: var(--mauve);
  }
  .brand {
    position: absolute;
    left: 520px;
    top: 62px;
    width: 340px;
    display: flex;
    align-items: center;
    justify-content: center;
    gap: 14px;
  }
  .brand-dot {
    width: 30px;
    height: 30px;
    border-radius: 50%;
    background: var(--teal);
    flex: none;
  }
  .brand-name {
    font-size: 34px;
    font-weight: 600;
    color: var(--mauve);
    letter-spacing: 0.2px;
    white-space: nowrap;
  }
  .tagline {
    position: absolute;
    left: 500px;
    top: 150px;
    width: 380px;
    text-align: center;
    font-size: 25px;
    font-weight: 700;
    color: var(--mauve);
  }
  .contact {
    position: absolute;
    left: 470px;
    top: 240px;
    color: var(--text-light);
  }
  .contact-name {
    font-size: 34px;
    font-weight: 700;
    line-height: 1.1;
  }
  .contact-role {
    font-size: 21px;
    font-weight: 600;
    margin-bottom: 26px;
  }
  .contact-line {
    font-size: 21px;
    font-weight: 600;
    line-height: 1.5;
  }
</style>
</head>
<body>
  <article class="card">
    <div class="card-photo" role="img" aria-label="Black and white photograph of two clasped hands wearing rings"></div>
    <div class="card-panel">
      <div class="panel-band"></div>
    </div>
    <svg class="panel-edge" width="900" height="514" viewBox="0 0 900 514" aria-hidden="true">
      <line x1="441" y1="0" x2="387" y2="514" stroke="var(--teal)" stroke-width="3"/>
    </svg>
    <div class="brand">
      <span class="brand-dot"></span>
      <span class="brand-name">The Tidewell Bureau</span>
    </div>
    <p class="tagline">Helping You Find The "One"</p>
    <div class="contact">
      <p class="contact-name">Maris Pelloway</p>
      <p class="contact-role">Matchmaker</p>
      <p class="contact-line">Tel. 0491 572 064</p>
      <p class="contact-line">maris@tidewellbureau.com.au</p>
      <p class="contact-line">www.tidewellbureau.com.au</p>
    </div>
  </article>
</body>
</html>
```